Breezeway Comfort business cards design

Need a business card design for a Heating and Air Conditioning business. I need these items included.
Business name: Breezeway Comfort
Owner: Marcus Tollefsen
License # 2874590
Phone number # 555-382-4071
Email: breezewaycomfortair@mailvista.example
Sales
Service
Installation
Maintenance

Heating and Air Conditioning

Requirements
Must have
• Company name , license number , phone number , email

```html
<!DOCTYPE html>
<html lang="en">
<head>
<meta charset="utf-8">
<title>Breezeway Comfort Business Cards</title>
<link rel="stylesheet" href="https://fonts.googleapis.com/css2?family=Montserrat:wght@400;500;700;800&display=swap">
<style>
  :root {
    --stage: #3b3b3b;
    --card: #ffffff;
    --brand-blue: #1c3f9e;
    --brand-orange: #f26b2a;
    --brand-red: #e6335a;
    --ink: #1f1f2a;
  }
  * { box-sizing: border-box; margin: 0; padding: 0; }
  html, body { width: 1200px; height: 689px; overflow: hidden; }
  body {
    background: var(--stage);
    font-family: "Montserrat", sans-serif;
    color: var(--ink);
    position: relative;
  }
  .card {
    position: absolute;
    top: 190px;
    width: 540px;
    height: 309px;
    background: var(--card);
    border-radius: 22px;
    box-shadow: 0 10px 30px rgba(0,0,0,.35);
  }
  .card--front { left: 40px; }
  .card--back { left: 620px; }

  /* Front */
  .front-brand {
    position: absolute;
    inset: 0;
    display: flex;
    align-items: center;
    justify-content: center;
    gap: 16px;
  }
  .brand-dot {
    width: 42px; height: 42px;
    border-radius: 50%;
    background: var(--brand-orange);
    flex: none;
  }
  .brand-name {
    color: var(--brand-blue);
    font-weight: 800;
    font-size: 36px;
    letter-spacing: .5px;
  }

  /* Back */
  .back-brand {
    position: absolute;
    left: 28px; top: 78px;
    width: 170px;
    display: flex;
    flex-direction: column;
    align-items: flex-start;
    gap: 10px;
  }
  .back-brand .brand-dot { width: 30px; height: 30px; }
  .back-brand .brand-name { font-size: 24px; line-height: 1.1; }

  .divider {
    position: absolute;
    left: 212px; top: 48px;
    width: 2px; height: 168px;
    background: linear-gradient(var(--brand-orange), var(--brand-red));
  }
  .contact {
    position: absolute;
    left: 230px; top: 46px;
    right: 16px;
  }
  .contact__name {
    color: var(--brand-blue);
    font-weight: 800;
    font-size: 24px;
    line-height: 1.1;
  }
  .contact__role {
    color: var(--brand-orange);
    font-size: 13px;
    font-weight: 500;
    margin-top: 2px;
  }
  .contact__license {
    font-size: 12.5px;
    margin-top: 18px;
  }
  .contact__line {
    display: flex;
    align-items: center;
    gap: 6px;
    font-size: 12.5px;
    margin-top: 10px;
  }
  .contact__line--email { font-size: 10.5px; margin-top: 6px; white-space: nowrap; }
  .contact__icon { width: 13px; height: 13px; flex: none; }

  .services {
    position: absolute;
    left: 0; right: 0; bottom: 30px;
    display: flex;
    justify-content: center;
    gap: 20px;
    list-style: none;
    font-size: 13.5px;
  }
  .services li { display: flex; align-items: center; gap: 6px; }
  .services li::before {
    content: "";
    width: 8px; height: 8px;
    border-radius: 50%;
    background: linear-gradient(135deg, var(--brand-orange), var(--brand-blue));
  }
</style>
</head>
<body>
  <section class="card card--front" aria-label="Card front">
    <div class="front-brand">
      <span class="brand-dot"></span>
      <span class="brand-name">Breezeway Comfort</span>
    </div>
  </section>

  <section class="card card--back" aria-label="Card back">
    <div class="back-brand">
      <span class="brand-dot"></span>
      <span class="brand-name">Breezeway<br>Comfort</span>
    </div>

    <div class="divider"></div>

    <div class="contact">
      <p class="contact__name">Marcus Tollefsen</p>
      <p class="contact__role">Owner</p>
      <p class="contact__license">License # 2874590</p>
      <p class="contact__line">
        <svg class="contact__icon" viewBox="0 0 16 16" aria-hidden="true">
          <path fill="var(--brand-red)" d="M3.5 1.5l2.2.4 1 3-1.5 1.2a8 8 0 0 0 4.7 4.7l1.2-1.5 3 1 .4 2.2c0 .8-.7 1.5-1.5 1.5A12 12 0 0 1 2 3c0-.8.7-1.5 1.5-1.5z"/>
        </svg>
        # 555-382-4071
      </p>
      <p class="contact__line contact__line--email">
        <svg class="contact__icon" viewBox="0 0 16 16" aria-hidden="true">
          <rect x="1" y="3" width="14" height="10" rx="1.5" fill="var(--brand-red)"/>
          <path d="M1.5 4l6.5 5 6.5-5" fill="none" stroke="#fff" stroke-width="1.3"/>
        </svg>
        breezewaycomfortair@mailvista.example
      </p>
    </div>

    <ul class="services">
      <li>Sales</li>
      <li>Service</li>
      <li>Installation</li>
      <li>Maintenance</li>
    </ul>
  </section>
</body>
</html>
```